DESSERT FLYER

We need a flyer design for desserts and drinks for our restaurant.

We use Retro/rustic as main theme

Flyer must include all images, which are attached to this project. We also named correctly for each images, so you can use for each dish's title (docx file)
Must include our logo as well.

Flyer tittle is "SWEET PLUMO"

Please see our website for reference at brickhollow.com.au

Flyer's printing size is A5 Vertical. Single Side

```html
<!DOCTYPE html>
<html lang="en">
<head>
<meta charset="utf-8">
<title>Sweet Plumo – Lantern Lane Dessert Flyer</title>
<link rel="stylesheet" href="https://fonts.googleapis.com/css2?family=Yellowtail&family=Courgette&family=Archivo+Black&family=Special+Elite&family=Fredoka:wght@600&display=swap">
<style>
  :root {
    --teal: #4fb3b7;
    --teal-deep: #2e9ea3;
    --orange: #f26a0f;
    --white: #ffffff;
    --plank-light: #e6e4dd;
    --plank-line: #c9c6bd;
    --wood-dark: #3b3026;
    --wood-mid: #574738;
    --shelf-green: #5d7a55;
    --floor: #a9a9a4;
  }
  * { box-sizing: border-box; margin: 0; padding: 0; }
  html, body { width: 862px; height: 1200px; overflow: hidden; background: var(--wood-dark); }
  .flyer { position: relative; width: 862px; height: 1200px; overflow: hidden; }

  .header-boards {
    position: absolute; left: 0; top: 0; width: 862px; height: 362px;
    background:
      repeating-linear-gradient(180deg, transparent 0 96px, var(--plank-line) 96px 100px),
      linear-gradient(180deg, #ecebe6, var(--plank-light));
  }
  .brand-name {
    position: absolute; left: 0; width: 100%; top: 92px; text-align: center;
    font-family: "Fredoka", sans-serif; font-weight: 600; font-size: 92px;
    letter-spacing: 6px; color: var(--teal-deep); line-height: 1;
  }
  .flyer-title {
    position: absolute; left: 0; width: 100%; top: 248px; text-align: center;
    font-family: "Yellowtail", cursive; font-size: 112px; color: var(--orange); line-height: 1;
  }

  .wood-wall {
    position: absolute; left: 0; top: 362px; width: 862px; height: 700px;
    background:
      repeating-linear-gradient(90deg, var(--wood-dark) 0 2px, transparent 2px 44px),
      linear-gradient(90deg, var(--wood-mid), #47392c 50%, var(--wood-mid));
  }
  .shelf-photo {
    position: absolute; left: 522px; top: 440px; width: 340px; height: 670px;
    background: linear-gradient(180deg, #5b5147, #4a4640 60%, #5d7a55 100%);
    border-left: 14px solid var(--shelf-green);
  }
  .floor {
    position: absolute; left: 0; top: 1062px; width: 862px; height: 138px;
    background: linear-gradient(180deg, #9d9d98, var(--floor));
  }

  .dish-photo {
    position: absolute; border: 7px solid var(--teal); border-radius: 50%;
    box-shadow: 0 3px 8px rgba(0,0,0,.4);
  }
  .dish-caption {
    position: absolute; width: 260px; text-align: center;
    font-family: "Courgette", cursive; font-size: 18px; line-height: 1.4;
    color: var(--white); text-shadow: 0 1px 3px rgba(0,0,0,.6);
  }
  .price {
    display: block; font-family: "Archivo Black", sans-serif; font-size: 24px;
    color: var(--orange); line-height: 1.1; text-shadow: none;
  }
  .price sup { font-size: 14px; }

  .contact {
    position: absolute; left: 548px; font-family: "Special Elite", monospace;
    font-size: 18px; color: var(--white); line-height: 1.35;
  }
</style>
</head>
<body>
<main class="flyer">
  <section class="header-boards">
    <div class="brand-name">LANTERN LANE</div>
    <h1 class="flyer-title">Sweet Plumo</h1>
  </section>

  <div class="wood-wall" role="img" aria-label="Weathered dark timber plank wall"></div>
  <div class="shelf-photo" role="img" aria-label="Rustic green shelf with teal bowls, white jug and cushions"></div>
  <div class="floor" role="img" aria-label="Grey concrete floor"></div>

  <div class="dish-photo" style="left:46px;top:388px;width:214px;height:132px;background:#b88a3a" role="img" aria-label="Banana fritters on a banana leaf"></div>
  <p class="dish-caption" style="left:22px;top:552px">Banana Fritter with<br>Vanilla Ice Cream<span class="price"><sup>$</sup>6.90</span></p>

  <div class="dish-photo" style="left:286px;top:430px;width:214px;height:132px;background:#c98a3c" role="img" aria-label="Fried ice cream in a glass bowl"></div>
  <p class="dish-caption" style="left:273px;top:594px">Fried Ice Cream with<br>Caramel/ Chocolate/<br>Strawberry Topping<span class="price"><sup>$</sup>6.90</span></p>

  <div class="dish-photo" style="left:46px;top:650px;width:214px;height:132px;background:#8fae6a" role="img" aria-label="Banana sago pudding on a leaf"></div>
  <p class="dish-caption" style="left:22px;top:814px">Banana Sago Pudding<br>with Peanut Topping<span class="price"><sup>$</sup>6.90</span></p>

  <div class="dish-photo" style="left:288px;top:716px;width:214px;height:132px;background:#9c6a48" role="img" aria-label="Fresh coconut with straw"></div>
  <p class="dish-caption" style="left:265px;top:876px">Fresh Coconut Juice<span class="price"><sup>$</sup>5.50</span></p>

  <div class="dish-photo" style="left:44px;top:912px;width:214px;height:132px;background:#c9a24a" role="img" aria-label="Black sticky rice with mango slices"></div>
  <p class="dish-caption" style="left:20px;top:1076px">Black Sticky Rice<br>with Mango<span class="price"><sup>$</sup>6.90</span></p>

  <div class="dish-photo" style="left:288px;top:946px;width:214px;height:132px;background:#7a5a3c" role="img" aria-label="Vietnamese drip coffee with beans"></div>
  <p class="dish-caption" style="left:265px;top:1104px">Vietnamese Coffee<span class="price"><sup>$</sup>6.90</span></p>

  <p class="contact" style="top:492px">www.brickhollow.com.au</p>
  <p class="contact" style="top:792px">18 Fernbrook Rd,<br>Westmere, 2071</p>
  <p class="contact" style="top:940px">
    <svg width="14" height="14" viewBox="0 0 24 24" aria-hidden="true"><circle cx="12" cy="12" r="11" fill="none" stroke="#fff" stroke-width="2"/><path d="M8 6c-1 2 0 6 3 9s6 4 8 3l-2-3-2 1c-1-1-3-3-4-4l1-2z" fill="#fff"/></svg>
    (02) 5550 1842</p>
</main>
</body>
</html>
```